Two documents one design language.

We are a small insurance broker who is committed to being open and transparent as possible with our customers.

For years, we have used plain word documents (see attachments) for our Policy Wording and our Terms of Business.

But now think we can do better and these plain documents are falling behind what our competitors are offering.

So we are now looking for both these documents to be professionally designed using the same design language for both.

We are putting few constraints on the design, but we do have some:
- It must be done in word as the wording can be changed at any time, so we must be able to maintain the documents ourselves.
- Any pictures or graphics you use must be royalty free so we can re-produce with any complications.
- Any pictures or graphics you use must been supplied as part of the package.
- You MUST NOT change any wording or grammar, it's not ours to change, its the insurers wording and HAS to be agreed with them.
- You must not split any any paragraph or bullet point over two pages.
- We are an insurance broker so what ever design you use, must look professional and inspire confidence... I.e. if you read it your thoughts turn to, these people are approachable, know what they are doing and will look after me.
- We specialise in musical instrument insurance, so we are looking for musical theming.

```html
<!DOCTYPE html>
<html lang="en">
<head>
<meta charset="utf-8">
<title>Policy Booklet Pages 20–29</title>
<link href="https://fonts.googleapis.com/css2?family=Montserrat:wght@700;800&family=Oswald:wght@300;400&family=Open+Sans:wght@400;600;700&display=swap" rel="stylesheet">
<style>
:root{
  --backdrop:#4b4b4b;
  --paper:#ffffff;
  --ink:#2f2f2f;
  --muted:#8a8a8a;
  --pink:#e8899c;
  --pink-deep:#c9566f;
  --pink-pale:#f7dde3;
  --grey-bar:#9c9c9c;
  --black:#111111;
  --link:#3b6fb3;
}
*{box-sizing:border-box;margin:0;padding:0}
html,body{width:1200px;height:4559px;overflow:hidden}
body{background:var(--backdrop);position:relative;font-family:"Open Sans",sans-serif;color:var(--ink)}
.range-title{position:absolute;left:0;top:18px;width:1200px;text-align:center;font-family:"Montserrat",sans-serif;font-weight:800;font-size:205px;line-height:1;color:#fff;letter-spacing:4px}
.page{position:absolute;width:482px;height:680px;background:var(--paper);overflow:hidden}
.col-left{left:115px}.col-right{left:615px}
.waves{position:absolute;left:0;right:0;top:300px;bottom:14px;background:linear-gradient(175deg,rgba(255,255,255,0) 0%,rgba(200,200,200,.25) 40%,rgba(170,170,170,.35) 75%,rgba(200,200,200,.2) 100%)}
.footer-bar{position:absolute;left:0;bottom:0;height:14px;width:100%;display:flex}
.footer-bar span{display:block;height:100%}
.bar-grey{background:var(--grey-bar)}.bar-pink{background:var(--pink)}.bar-black{background:var(--black)}
.page-tab{position:absolute;top:0;width:40px;height:22px;font-size:10px;font-weight:700;color:#fff;display:flex;align-items:center;justify-content:center}
.col-left .page-tab{left:0;background:var(--grey-bar)}
.col-right .page-tab{right:0;background:var(--pink)}
.brand{position:absolute;top:14px;font-weight:700;font-size:8px;line-height:1.15;color:var(--pink-deep);letter-spacing:.6px;text-align:center}
.col-left .brand{left:75px}.col-right .brand{left:300px}
.doc-label{position:absolute;top:24px;font-size:6px;color:var(--muted);letter-spacing:.8px;font-weight:600}
.col-left .doc-label{left:185px}.col-right .doc-label{left:225px}
.content{position:relative;z-index:1;padding:78px 40px 0 55px;font-size:7.2px;line-height:1.75}
.col-right .content{padding:78px 45px 0 45px}
.content p{margin-bottom:7px}
.content ol,.content ul{margin:0 0 7px 14px}
.content li{margin-bottom:5px}
.center{text-align:center;font-weight:700}
.bold{font-weight:700}
.red{color:#d23c4c}
.blue{color:var(--link)}
.section-title{display:flex;gap:10px;margin:0 0 18px -10px}
.section-title::before{content:"";width:3px;background:var(--grey-bar)}
.section-title h2{font-family:"Oswald",sans-serif;font-weight:300;font-size:24px;line-height:1.05;color:#555;text-transform:uppercase}
.addr p{margin-bottom:4px}
.photo{position:absolute;z-index:1}
.back-pink{position:absolute;left:0;top:0;width:150px;height:360px;background:var(--pink)}
.back-art{position:absolute;left:150px;top:0;width:332px;height:360px;background:radial-gradient(circle at 55% 45%,var(--pink-pale),#fff 70%)}
.back-photo{position:absolute;left:0;top:360px;width:240px;height:240px;background:linear-gradient(135deg,#1f5e4c 0%,#2b2b2b 45%,#b78d3b 70%,#5a4420 100%)}
.back-dark{position:absolute;left:240px;top:360px;width:242px;height:240px;background:linear-gradient(160deg,#2a2a2a,#111 60%,#2e2e2e)}
.back-footer{position:absolute;left:0;top:600px;width:482px;height:66px;display:flex;justify-content:space-between;align-items:center;padding:0 35px;font-size:6.5px;line-height:1.5}
.back-footer .brand{position:static;font-size:10px}
.back-contact{text-align:right;line-height:2}
</style>
</head>
<body>

<div class="range-title">20-29</div>

<!-- Page 20 -->
<section class="page col-left" style="top:298px">
  <div class="waves" role="img" aria-label="Soft wave line pattern"></div>
  <div class="page-tab">20</div>
  <div class="brand">HARLOW BROOK<br>INSURANCE</div>
  <div class="doc-label">POLICY BOOKLET</div>
  <div class="content">
    <ol start="3">
      <li><b>YOU</b> must notify the police as soon as it is reasonably possible in the event of any loss, destruction or damage by theft, attempted theft or malicious damage.</li>
      <li>Automatic reinstatement of cover, following a claim being made, is included under this policy without any additional premium becoming payable.</li>
      <li><b>YOU</b> should be aware that a claim arising after the renewal of <b>YOUR</b> policy has been incurred might affect the assessment and acceptance of renewal by <b>YOUR</b> insurers.</li>
    </ol>
    <p class="center">OUR RIGHTS</p>
    <ol>
      <li><b>WE</b> may –
        <ul><li>take full responsibility for conducting, defending or settling any claim in <b>YOUR</b> name</li><li>take any action <b>WE</b> may consider necessary to enforce <b>YOUR</b> rights or <b>OUR</b> rights under this insurance.</li></ul></li>
      <li>Following loss or damage, <b>WE</b> will be entitled at <b>OUR</b> sole option to repair, replace or pay for any item covered by this insurance.
        <p>For total loss or destruction of any article, <b>WE</b> will pay <b>YOU</b> the cost of replacing the item as new, as long as:</p>
        <ul><li>the new item is as close as possible to, but not an improvement on, the original item when it was new;</li><li>the sum insured covers the full cost of the item; and</li><li><b>YOU</b> have paid or <b>WE</b> have authorised the cost of replacement.</li></ul></li>
      <li>In the event of a claim, <b>WE</b> will not pay more than the sum insured specified in the <b>SCHEDULE</b>.</li>
      <li>If the total value of the items, at the time of loss or damage, is more than <b>YOUR</b> sum insured for such items, then <b>WE</b> will only pay for a proportion of the claim.
        <p>For example – If <b>YOUR</b> sum insured only represents one half of the total value of items <b>WE</b> will only pay one half of the cost of repair or replacement.</p></li>
    </ol>
  </div>
  <div class="footer-bar"><span class="bar-grey" style="width:150px"></span><span class="bar-pink" style="flex:1"></span></div>
</section>

<!-- Page 21 -->
<section class="page col-right" style="top:298px">
  <div class="waves" role="img" aria-label="Soft wave line pattern"></div>
  <div class="page-tab">21</div>
  <div class="doc-label">2024</div>
  <div class="brand">HARLOW BROOK<br>INSURANCE</div>
  <div class="content">
    <p>5. Following a valid claim, <b>WE</b> may, without incurring any further liability and without diminishing <b>YOUR</b> right to rely on any condition of this insurance, take and keep possession of any of the <b>PROPERTY INSURED</b> and to deal with salvage in a reasonable manner, but <b>YOU</b> may not abandon any property to <b>US</b>.</p>
    <p>6. If at the time of any loss, damage or liability arising under this policy there is any other insurance covering the same loss, damage or liability <b>WE</b> will only pay <b>OUR</b> rateable proportion.</p>
    <p class="bold">FRAUD</p>
    <p>If <b>YOU</b> make a fraudulent claim under this insurance contract, then <b>WE</b>:</p>
    <p>(a) Are not liable to pay the claim; and</p>
    <p>(b) May recover from <b>YOU</b> any sums paid by <b>US</b> to <b>YOU</b> in respect of the claim; and</p>
    <p>(c) May by notice to <b>YOU</b> treat the contract as having been terminated with effect from the time of the fraudulent act.</p>
    <p style="margin-left:14px">If <b>WE</b> exercise <b>OUR</b> right under clause (c) above:</p>
    <p>(a) <b>WE</b> will not be liable to <b>YOU</b> in respect of a relevant event occurring after the time of the fraudulent act. A relevant event is whatever gives rise to <b>OUR</b> liability under the insurance contract (such as the occurrence of a loss, the making of a claim, or the notification of a potential claim); and</p>
    <p>(b) <b>WE</b> need not return any of the premiums paid.</p>
  </div>
  <div class="footer-bar"><span class="bar-pink" style="width:295px"></span><span class="bar-black" style="flex:1"></span></div>
</section>

<!-- Page 22 -->
<section class="page col-left" style="top:1003px">
  <div class="waves" role="img" aria-label="Soft wave line pattern"></div>
  <div class="page-tab">22</div>
  <div class="brand">HARLOW BROOK<br>INSURANCE</div>
  <div class="doc-label">POLICY BOOKLET</div>
  <div class="content" style="font-size:6.8px;line-height:1.7">
    <div class="section-title"><h2>How to make<br>a complaint</h2></div>
    <p><b>OUR</b> aim is to provide all <b>OUR</b> customers with a first-class standard of service. However, there may be occasions when <b>YOU</b> feel this objective has not been achieved. If <b>YOU</b> have a complaint about <b>YOUR</b> policy or the handling of a claim, the details below set out some of the key steps that <b>YOU</b> can take to address <b>YOUR</b> concerns.</p>
    <p>Please quote <b>YOUR</b> Policy Number in all correspondence so that <b>YOUR</b> concern may be dealt with speedily.</p>
    <p class="bold">Where do I start?</p>
    <p>If <b>YOUR</b> complaint is about the way in which the policy was sold to <b>YOU</b> or whether it meets <b>YOUR</b> requirements, <b>YOU</b> should contact:</p>
    <div class="addr">
      <p>Harlow Brook Insurance Services</p><p>12 Linden Walk</p><p>Ashcombe</p><p>Pelham, Wessex, PL4 7QD</p>
      <p>EMAIL: <span class="red">complaints@harlowbrook.co.uk</span></p><p>Telephone: 0123 456 7890</p>
    </div>
    <p style="margin-top:6px">If <b>YOUR</b> complaint is about a claim, <b>YOU</b> should refer the matter to the Fenwick Underwriting Claims Team at KPL Claims Management Ltd. Their contact details are provided below.</p>
    <div class="addr">
      <p>KPL Claims Management Ltd</p><p>The Quays</p><p>Harbour Road</p><p>Marlow Sands</p><p>MS1 4QQ</p><p>Telephone: 0123 456 7811</p>
      <p>Email: <span class="red">claims@kplclaims.example</span></p>
    </div>
    <p style="margin-top:6px">If <b>YOUR</b> complaint is about anything else, <b>YOU</b> should refer it to Fenwick Underwriting, whose contact details are:</p>
  </div>
  <div class="footer-bar"><span class="bar-grey" style="width:150px"></span><span class="bar-pink" style="flex:1"></span></div>
</section>

<!-- Page 23 -->
<section class="page col-right" style="top:1003px">
  <div class="waves" role="img" aria-label="Soft wave line pattern"></div>
  <div class="page-tab">23</div>
  <div class="doc-label">2024</div>
  <div class="brand">HARLOW BROOK<br>INSURANCE</div>
  <div class="content" style="font-size:6.8px;line-height:1.7">
    <div class="addr">
      <p>Complaints Manager</p><p>Fenwick Underwriting</p><p>Suite 4, Gallery 2</p><p>Merchant House</p><p>9 Cloth Row</p><p>Pelham, PL1 7DD</p><p>Telephone: 0123 456 2010</p>
      <p>Email: <span class="red">complaints@fenwickuw.example</span></p>
    </div>
    <p style="margin-top:8px">Alternatively <b>YOU</b> can ask <b>YOUR</b> broker to refer the matter on for <b>YOU</b>.</p>
    <p class="bold" style="margin-top:8px">What happens next?</p>
    <p>If KPL or Fenwick Underwriting are not able to resolve <b>YOUR</b> complaint satisfactorily by close of business of the third business day following, they will refer <b>YOUR</b> complaint to the Complaints Manager at Calder Specialty Ltd, who will send <b>YOU</b> an acknowledgement letter.</p>
    <p>If <b>YOU</b> don't receive any acknowledgement letter, or at any time if <b>YOU</b> wish to do so, <b>YOU</b> may contact the Complaints Manager <b>YOURSELF</b> by writing to:</p>
    <div class="addr">
      <p>Complaints Manager</p><p>Calder Specialty Ltd</p><p>1 Mercer Yard</p><p>Pelham</p><p>PL3 5NN</p><p>Telephone: 0123 456 7444</p>
      <p>E-mail: <span class="red">COMPLAINTS@CALDERSPECIALTY.EXAMPLE</span></p>
    </div>
    <p style="margin-top:8px">The Complaints Manager will investigate <b>YOUR</b> complaint and will provide <b>YOU</b> with a written response within eight weeks of <b>YOUR</b> initial complaint. This will either be a final response or a letter informing <b>YOU</b> that <b>WE</b> need more time for <b>OUR</b> investigation.</p>
    <p class="bold">If YOU remain unhappy</p>
    <p>If <b>WE</b> have not resolved <b>YOUR</b> complaint at the end of eight weeks, or if after receiving <b>OUR</b> final response <b>YOU</b> remain dissatisfied, <b>YOU</b> may be able to refer <b>YOUR</b> complaint to the Consumer Redress Service (contact details below). <b>YOU</b> will have six months from the date of the final response to make this referral.</p>
  </div>
  <div class="footer-bar"><span class="bar-pink" style="width:295px"></span><span class="bar-black" style="flex:1"></span></div>
</section>

<!-- Page 24 -->
<section class="page col-left" style="top:1708px">
  <div class="waves" role="img" aria-label="Soft wave line pattern"></div>
  <div class="page-tab">24</div>
  <div class="brand">HARLOW BROOK<br>INSURANCE</div>
  <div class="doc-label">POLICY BOOKLET</div>
  <div class="content" style="font-size:6px;line-height:1.7">
    <p><b>YOUR</b> rights as a customer to take legal action are not affected by the existence or use of the complaints procedure mentioned above. However, the Consumer Redress Service may not adjudicate on a case where court proceedings are actively in progress.</p>
    <div class="addr" style="margin-top:14px">
      <p>The Consumer Redress Service, Mill Wharf</p><p>Quayside House</p><p>Pelham PL4 9SR</p><p style="margin-top:6px">Telephone: 0800 000 0123</p>
    </div>
    <p style="margin-top:6px">Further information is available from them and <b>YOU</b> may refer a complaint to them online at <b>www.consumer-redress.example</b>.</p>
    <p>The Service will only review complaints from eligible complainants. An eligible complainant is defined as:</p>
    <ol>
      <li>a private individual;</li>
      <li>a business which has a group annual turnover of less than £6.5m (approx. £5.2m) and either:
        <ol type="a"><li>fewer than 50 staff; or</li><li>an annual balance sheet total of less than £5m at the time the complainant refers the complaint to the respondent;</li></ol></li>
      <li>a charity which has an annual income of less than £6.5m at the time the complainant refers the complaint to the respondent; or</li>
      <li>a trustee of a trust which has a net asset value of less than £5m at the time the complainant refers the complaint to the respondent.</li>
    </ol>
    <p class="bold" style="margin-top:10px">Insurer Public Register</p>
    <p>The Insurer Public Register can be checked by visiting the Financial Standards Authority website on <span class="red">www.fsa-register.example</span> or by calling 0800 000 6768.</p>
    <p class="bold" style="margin-top:6px">Policyholder Compensation Scheme (PCS)</p>
    <p>Northmere Insurance UK Ltd is covered by the PCS. This means that <b>YOU</b> may be entitled to compensation from the scheme in the unlikely event that Northmere Insurance UK Ltd cannot meet its obligations. Further details can be obtained from:</p>
    <div class="addr" style="display:grid;grid-template-columns:1fr 1fr">
      <p>PCS</p><p></p><p>PO Box 410</p><p></p><p>Millbrook</p><p></p><p>Pelham PL11 0JJ</p><p></p><p>Telephone</p><p>0800 000 7100</p><p>Website</p><p class="red">www.pcs.example/contact</p>
    </div>
  </div>
  <div class="footer-bar"><span class="bar-grey" style="width:150px"></span><span class="bar-pink" style="flex:1"></span></div>
</section>

<!-- Page 25 -->
<section class="page col-right" style="top:1708px">
  <div class="waves" role="img" aria-label="Soft wave line pattern"></div>
  <div class="page-tab">25</div>
  <div class="doc-label">2024</div>
  <div class="brand">HARLOW BROOK<br>INSURANCE</div>
  <div class="content" style="font-size:6.2px;line-height:1.75;padding-top:70px">
    <div class="section-title"><h2>Claims conditions</h2></div>
    <p class="bold" style="margin-top:10px">Northmere Insurance UK Limited</p>
    <p>Northmere Insurance UK Limited is a company incorporated in England and Wales with company number 00000001 and registered office address is 3 Mercer Yard, Pelham, PL3 5NN. Northmere Insurance UK Limited is authorised by the Prudential Standards Authority and regulated by the Financial Standards Authority and the Prudential Standards Authority. Firm Reference Number 000001. <b>YOU</b> can check this on the Insurer Public Register by visiting <span class="red">https://register.example/</span>.</p>
    <p class="bold" style="margin-top:12px">Calder Specialty Limited</p>
    <p>Calder Specialty Limited is a company incorporated in England and Wales with company number 00000002 and registered office address is 1 Mercer Yard, Pelham, PL3 5NN. Calder Specialty Limited is authorised and regulated by the Financial Standards Authority. Firm Reference Number 000002. <b>YOU</b> can check this on the Insurer Public Register by visiting <span class="red">https://register.example/</span>.</p>
  </div>
  <div class="photo" role="img" aria-label="Photograph of a piano keyboard beside a drum" style="left:15px;top:352px;width:208px;height:284px;background:linear-gradient(160deg,#1a1a1a 0%,#3a3a3a 35%,#7a4a22 65%,#c08a4a 100%)"></div>
  <div class="photo" role="img" aria-label="Photograph of an acoustic guitar in a bright room" style="left:228px;top:522px;width:120px;height:114px;background:linear-gradient(180deg,#f1f1ef,#d9d1c4 60%,#9a7048)"></div>
  <div class="photo" role="img" aria-label="Photograph of hands playing a digital keyboard" style="left:354px;top:522px;width:118px;height:114px;background:linear-gradient(180deg,#e9e9e9,#bdbdbd 55%,#3a3a3a)"></div>
  <div class="footer-bar"><span class="bar-pink" style="width:295px"></span><span class="bar-black" style="flex:1"></span></div>
</section>

<!-- Page 26 -->
<section class="page col-left" style="top:2415px">
  <div class="waves" role="img" aria-label="Soft wave line pattern"></div>
  <div class="page-tab">26</div>
  <div class="brand">HARLOW BROOK<br>INSURANCE</div>
  <div class="doc-label">POLICY BOOKLET</div>
  <div class="content" style="font-size:5.5px;line-height:1.5;padding-top:72px">
    <div class="section-title" style="margin-bottom:12px"><h2>Privacy<br>notices</h2></div>
    <p class="blue">Fenwick Insurance Management Ltd – Privacy Notice</p>
    <p>Fenwick Insurance Management Ltd (t/a Fenwick Underwriting) processes certain information in connection with this policy. Information that Fenwick Underwriting processes may be defined as personal and/or sensitive personal information.</p>
    <p>For more detailed information, please visit Fenwick Underwriting's full privacy notice set out at <span class="blue">www.fenwickuw.example/privacy-notice</span></p>
    <p class="blue">Northmere Insurance UK Limited &amp; Calder Specialty Limited – Privacy Notice</p>
    <p class="blue">Information WE process</p>
    <p><b>WE</b> process certain information in connection with this policy. Information <b>WE</b> process may be defined as personal and/or sensitive information.</p>
    <p>Personal information is information about a living, identifiable individual e.g., name, address, driving licence or national insurance number. Personal information also includes information about an individual which can be identified through a work function or their title.</p>
    <p>In addition, personal information may contain sensitive personal information, such as information about <b>YOUR</b> health and/or any criminal convictions.</p>
    <p>In this privacy notice, <b>WE</b>, <b>US</b> and <b>OUR</b> means Northmere Insurance UK Limited and Calder Specialty Limited on behalf of Northmere Insurance UK Limited, in so far as this notice relates to their processing of personal data.</p>
    <p><b>WE</b> each act as controller in relation to <b>OUR</b> processing of personal and/or sensitive personal information and <b>WE</b> will each hold and otherwise process such information in compliance with <b>OUR</b> obligations under UK data privacy laws for the purposes set out in this notice. For more detailed information please review the relevant privacy notice.</p>
    <p class="bold">Northmere Insurance UK Limited privacy notice:</p>
    <p class="blue">www.northmere.example/legal/privacy-notice</p>
    <p class="bold">Calder Specialty Limited privacy notice:</p>
    <p class="blue">www.calderspecialty.example/privacy-policy</p>
    <p><b>YOU</b> should show this notice to any other individual (a data subject) whose personal data <b>YOU</b> share with <b>US</b>.</p>
    <p class="blue">Collecting electronic information</p>
    <p>If <b>YOU</b> contact <b>US</b> via an electronic method, <b>WE</b> may record <b>YOUR</b> internet protocol (IP) address. <b>YOUR</b> telephone company may also provide <b>US</b> with <b>YOUR</b> telephone number.</p>
    <p class="bold">How WE use YOUR personal information</p>
    <p><b>YOUR</b> personal and/or sensitive personal information <b>WE</b> receive in connection with this policy may be used by <b>US</b> in a number of ways, including to:</p>
    <ul><li>arrange and administer an application for insurance;</li><li>manage and administer the insurance;</li><li>investigate, process, and manage claims;</li><li>prevent and detect crime (including fraud);</li><li>offer renewals;</li><li>develop new products; and/or</li><li>conduct research (and for wider statistical purposes).</li></ul>
  </div>
  <div class="footer-bar"><span class="bar-grey" style="width:150px"></span><span class="bar-pink" style="flex:1"></span></div>
</section>

<!-- Page 27 -->
<section class="page col-right" style="top:2415px">
  <div class="waves" role="img" aria-label="Soft wave line pattern"></div>
  <div class="page-tab">27</div>
  <div class="doc-label">2024</div>
  <div class="brand">HARLOW BROOK<br>INSURANCE</div>
  <div class="content" style="font-size:5.5px;line-height:1.5;padding-top:64px">
    <p>For information on the lawful bases <b>WE</b> rely on to process <b>YOUR</b> personal and/or sensitive personal information for these purposes please see the relevant notices above.</p>
    <p class="blue">Who WE share YOUR information with</p>
    <p><b>WE</b> may pass <b>YOUR</b> personal and/or sensitive personal information <b>WE</b> receive in connection with this Policy to industry-related third parties, including authorised agents; service providers; reinsurers; other insurers; legal advisers; loss adjusters and claims handlers for the purposes above.</p>
    <ol><li><b>WE</b> may also share personal and/or sensitive personal information <b>WE</b> receive in connection with this policy with regulatory bodies such as the Financial Standards Authority (FSA) for the purposes of administering and regulating <b>YOUR</b> insurance.</li></ol>
    <p><b>WE</b> may also share <b>YOUR</b> personal and/or sensitive personal information with law enforcement, fraud detection, credit reference and debt collection agencies and within the Northmere / Calder / Ostrand Re Group of companies to:</p>
    <ul><li>assess financial and insurance risks;</li><li>recover debt;</li><li>to prevent and detect crime; and/or</li><li>develop products and services</li></ul>
    <p>Except for the disclosures described above and in <b>OUR</b> full privacy notice, <b>WE</b> will not disclose <b>YOUR</b> personal and/or sensitive personal information to anyone outside the Northmere / Calder / Ostrand Re Group of companies except:</p>
    <ul><li>where <b>WE</b> have <b>YOUR</b> permission to do so;</li><li>where <b>WE</b> are required or permitted to do so by law;</li><li>to other companies where required in connection with the provision of a service to <b>US</b> or <b>YOU</b>; and/or</li><li>where <b>WE</b> transfer rights and obligations under the insurance provided under this Policy.</li></ul>
    <p class="blue">The transferring of personal information outside the United Kingdom</p>
    <p>In providing insurance services, <b>WE</b> may transfer <b>YOUR</b> personal and/or sensitive personal information to other countries including countries outside the United Kingdom. If this happens, it will at all times be held securely and handled in accordance with UK data privacy laws.</p>
    <p class="blue">Access to YOUR information</p>
    <p><b>YOU</b> have a right to know what personal and/or sensitive personal information <b>WE</b> hold about <b>YOU</b>. If <b>YOU</b> would like to know what information <b>WE</b> hold, please contact the Data Protection Officer at the address listed within this notice. <b>WE</b> may need to confirm <b>YOUR</b> identity before <b>WE</b> can respond to <b>YOUR</b> request.</p>
    <p>If <b>WE</b> do hold information about <b>YOU</b>, <b>WE</b> will:</p>
    <p>give <b>YOU</b> a description of it;</p>
    <ul><li>give <b>YOU</b> a description of it;</li><li>tell <b>YOU</b> why <b>WE</b> are holding it;</li><li>tell <b>YOU</b> who it could be disclosed to; and</li><li>let <b>YOU</b> have a copy of the information in an intelligible form.</li></ul>
    <p>If some of <b>YOUR</b> information is inaccurate, <b>YOU</b> can ask <b>US</b> to correct any mistakes by contacting <b>OUR</b> Data Protection Officer.</p>
  </div>
  <div class="footer-bar"><span class="bar-pink" style="width:295px"></span><span class="bar-black" style="flex:1"></span></div>
</section>

<!-- Page 28 -->
<section class="page col-left" style="top:3120px">
  <div class="waves" role="img" aria-label="Soft wave line pattern"></div>
  <div class="page-tab">28</div>
  <div class="brand">HARLOW BROOK<br>INSURANCE</div>
  <div class="doc-label">POLICY BOOKLET</div>
  <div class="content" style="font-size:6px;line-height:1.75;padding-top:88px">
    <p class="blue">Data subject rights</p>
    <p>Under UK data privacy laws, data subjects have certain rights in relation to their personal information, including a right of access (see above), a right to correct or supplement inaccurate / incomplete information, a right to request the deletion of information, a right to request the suspension of the processing of the information, a data portability right and a right to object to <b>OUR</b> processing of the personal information. These rights may only be available in certain circumstances and are subject to certain exemptions.</p>
    <p>For more information about <b>YOUR</b> data subject rights please see the relevant privacy notice above or contact <b>US</b> using the details provided below.</p>
    <p class="blue">Data Retention</p>
    <p><b>WE</b> keep <b>YOUR</b> personal and/or sensitive personal information for as long as is reasonably required for the purposes explained in this notice. <b>WE</b> also keep records to meet legal, regulatory, tax or accounting needs. For example, <b>WE</b> are required to retain an accurate record of <b>YOUR</b> dealings with <b>US</b>, so <b>WE</b> can respond to any complaints or challenges <b>YOU</b> or others might raise later. The specific retention period will depend on <b>YOUR</b> relationship with <b>US</b>. Please contact <b>US</b> using the details below for more information on specific retention periods.</p>
    <p class="blue">Changes to this Notice</p>
    <p><b>WE</b> keep <b>OUR</b> privacy notice(s) under regular review. <b>WE</b> would encourage <b>YOU</b> to check back regularly for updates. The Northmere Insurance UK notice was last updated in May 2024. The Calder Specialty UK Ltd notice was last updated in September 2024.</p>
    <p class="blue">Contacting Us</p>
    <p>If <b>YOU</b> have any questions relating to the processing of <b>YOUR</b> personal information and/or sensitive personal information, contact:</p>
    <div class="addr" style="display:grid;grid-template-columns:110px 1fr">
      <p style="grid-column:1/3">Data Protection Officer</p><p style="grid-column:1/3" class="bold">Calder Specialty Limited</p><p style="grid-column:1/3">1 Mercer Yard</p><p style="grid-column:1/3">Pelham</p><p style="grid-column:1/3">PL3 5NN</p>
      <p>Telephone</p><p>0123 456 5825</p><p>Email</p><p class="red">dataprotection@calderspecialty.example</p>
    </div>
  </div>
  <div class="footer-bar"><span class="bar-grey" style="width:150px"></span><span class="bar-pink" style="flex:1"></span></div>
</section>

<!-- Page 29 -->
<section class="page col-right" style="top:3120px">
  <div class="waves" role="img" aria-label="Soft wave line pattern"></div>
  <div class="page-tab">29</div>
  <div class="doc-label">2024</div>
  <div class="brand">HARLOW BROOK<br>INSURANCE</div>
  <div class="footer-bar"><span class="bar-pink" style="width:295px"></span><span class="bar-black" style="flex:1"></span></div>
</section>

<!-- Back cover -->
<section class="page col-left" style="top:3826px">
  <div class="back-pink"></div>
  <div class="back-art" role="img" aria-label="Faint pink line illustration of a cherub playing a harp"></div>
  <div class="back-photo" role="img" aria-label="Photograph of a saxophone on green and white cloth"></div>
  <div class="back-dark" role="img" aria-label="Dark panel with fine diagonal line texture"></div>
  <div class="back-footer">
    <div>Harlow Brook Insurance Services<br>12 Linden Walk<br>Ashcombe<br>Pelham<br>Wessex<br>PL4 7QD</div>
    <div class="brand">HARLOW BROOK<br>INSURANCE</div>
    <div class="back-contact">0123 456 7890<br>INSURE@HARLOWBROOK.CO.UK<br>WWW.HARLOWBROOK.CO.UK</div>
  </div>
  <div class="footer-bar"><span class="bar-grey" style="width:150px"></span><span class="bar-pink" style="flex:1"></span></div>
</section>

</body>
</html>
```